Reiki business card

Please see uploaded files. There is a word document on there explaining what is required and what the other uploaded files are for. I am after a soft, relaxing, warm welcoming feel to the card. Thank you.

Business

```html
<!DOCTYPE html>
<html lang="en">
<head>
<meta charset="utf-8">
<title>Tavia For Children &amp; Animals – Business Card</title>
<link href="https://fonts.googleapis.com/css2?family=Noto+Sans:ital,wght@1,700&display=swap" rel="stylesheet">
<style>
  :root {
    --stage: #161514;
    --teal: #0bbbd1;
    --teal-light: #4fcfe0;
    --teal-soft: #8fdfea;
    --teal-deep: #21a8c4;
    --ink: #ffffff;
  }
  html, body {
    margin: 0;
    padding: 0;
    width: 1200px;
    height: 1000px;
    overflow: hidden;
    background: var(--stage);
  }
  .stage {
    position: relative;
    width: 1200px;
    height: 1000px;
  }
  .card {
    position: absolute;
    left: 301px;
    width: 600px;
    height: 370px;
    overflow: hidden;
    background: linear-gradient(90deg, var(--teal-light) 0%, var(--teal) 45%, var(--teal) 100%);
    font-family: "Noto Sans", Verdana, sans-serif;
    font-style: italic;
    font-weight: 700;
    color: var(--ink);
  }
  .card--front { top: 104px; }
  .card--back { top: 544px; }
  .card__glow {
    position: absolute;
    left: 20px;
    top: 0;
    width: 160px;
    height: 260px;
    border-radius: 50%;
    background: radial-gradient(ellipse at center, rgba(143,223,234,0.55) 0%, rgba(143,223,234,0) 70%);
  }
  .card__leaf-art {
    position: absolute;
    left: 80px;
    top: 90px;
    width: 240px;
    height: 280px;
    border-radius: 45% 45% 40% 40%;
    background: radial-gradient(ellipse at 50% 50%, rgba(143,223,234,0.6) 0%, rgba(143,223,234,0.25) 55%, rgba(143,223,234,0) 75%);
  }
  .card__silhouette-art {
    position: absolute;
    left: 300px;
    top: 110px;
    width: 300px;
    height: 260px;
    border-radius: 45% 45% 0 0;
    background: radial-gradient(ellipse at 45% 55%, rgba(33,168,196,0.85) 0%, rgba(33,168,196,0.55) 50%, rgba(33,168,196,0) 78%);
  }
  .card__title {
    position: absolute;
    right: 54px;
    top: 34px;
    margin: 0;
    font-size: 37px;
    line-height: 50px;
    text-align: right;
    font-weight: 700;
  }
  .card__contact {
    position: absolute;
    left: 328px;
    top: 290px;
    margin: 0;
    font-size: 21px;
    line-height: 28px;
  }
  .card__tagline {
    position: absolute;
    left: 0;
    right: 0;
    top: 34px;
    margin: 0;
    font-size: 25px;
    line-height: 33px;
    text-align: center;
  }
  .card__email {
    position: absolute;
    left: 83px;
    top: 311px;
    margin: 0;
    font-size: 17px;
  }
</style>
</head>
<body>
<main class="stage">
  <section class="card card--front">
    <div class="card__glow"></div>
    <div class="card__leaf-art" role="img" aria-label="Skeleton leaf photograph in pale aqua"></div>
    <div class="card__silhouette-art" role="img" aria-label="Soft silhouette of a child with a dog"></div>
    <h1 class="card__title">Tavia For Children<br>&amp; Animals</h1>
    <p class="card__contact">Marla Fenwick<br>0400 218 764</p>
  </section>

  <section class="card card--back">
    <div class="card__glow"></div>
    <div class="card__leaf-art" role="img" aria-label="Skeleton leaf photograph in pale aqua"></div>
    <div class="card__silhouette-art" role="img" aria-label="Soft silhouette of a child with a dog"></div>
    <p class="card__tagline">Reiki - relaxes, restores balance<br>&amp; promotes healing</p>
    <p class="card__email">taviachildrenandpets@example.com</p>
  </section>
</main>
</body>
</html>
```